Tech business card design

We need an amazing business card design for our new business 'Brakka' a marketing tech startup based in Sydney, Australia. We provide an online marketplace for businesses to search and buy advertising media, connect with service providers and learn more about marketing. We wish to communicate 'cool tech', reliability and professionalism and design based around our logo.

Target Market(s)

Business Owners

Contact Information for Business Card

Name
Position
Email Address
Website
Phone Number

Font styles to use
Other font styles liked:
• Avenir & Avenir Next

Colors

Designer to choose colors to be used in the design.

```html
<!DOCTYPE html>
<html lang="en">
<head>
<meta charset="utf-8">
<title>Brakka Business Card</title>
<link href="https://fonts.googleapis.com/css2?family=Nunito+Sans:wght@300;400;800&display=swap" rel="stylesheet">
<style>
  :root {
    --page-bg: #ffffff;
    --card-edge: #6e6e6e;
    --panel-light: #ffffff;
    --panel-navy: #0f0e38;
    --ink-navy: #0f0e38;
    --text-light: #ffffff;
    --watermark: rgba(255, 255, 255, 0.11);
  }
  html, body {
    margin: 0;
    padding: 0;
    width: 1200px;
    height: 1000px;
    overflow: hidden;
    background: var(--page-bg);
    font-family: "Nunito Sans", "Avenir Next", Avenir, sans-serif;
  }
  .canvas {
    position: relative;
    width: 1200px;
    height: 1000px;
  }
  .card {
    position: absolute;
    left: 100px;
    top: 194px;
    width: 1000px;
    height: 612px;
    box-sizing: border-box;
    border: 1px solid var(--card-edge);
    overflow: hidden;
    display: flex;
  }
  .brand-panel {
    width: 412px;
    height: 100%;
    background: var(--panel-light);
    display: flex;
    align-items: center;
    padding-left: 50px;
    box-sizing: border-box;
  }
  .brand-name {
    font-weight: 800;
    font-size: 104px;
    line-height: 1;
    letter-spacing: -2px;
    color: var(--ink-navy);
    margin-top: 4px;
  }
  .info-panel {
    position: relative;
    flex: 1;
    height: 100%;
    background: var(--panel-navy);
    color: var(--text-light);
    overflow: hidden;
  }
  .brand-watermark {
    position: absolute;
    left: -8px;
    top: 168px;
    font-weight: 800;
    font-size: 250px;
    line-height: 1;
    letter-spacing: -4px;
    color: var(--watermark);
    white-space: nowrap;
  }
  .person {
    position: absolute;
    right: 48px;
    top: 50px;
    text-align: right;
  }
  .person-name {
    font-weight: 300;
    font-size: 50px;
    line-height: 58px;
    margin: 0;
  }
  .person-role {
    font-weight: 300;
    font-size: 33px;
    line-height: 40px;
    margin: 0;
  }
  .contact {
    position: absolute;
    right: 48px;
    top: 444px;
    text-align: right;
    font-weight: 300;
    font-size: 30px;
    line-height: 42px;
    margin: 0;
    padding: 0;
    list-style: none;
  }
</style>
</head>
<body>
  <main class="canvas">
    <article class="card">
      <section class="brand-panel">
        <div class="brand-name">brakka</div>
      </section>
      <section class="info-panel">
        <div class="brand-watermark" aria-hidden="true">brakka</div>
        <div class="person">
          <p class="person-name">Nadia Kerr</p>
          <p class="person-role">Founder, Director</p>
        </div>
        <ul class="contact">
          <li>+61 (0)412 580 236</li>
          <li>nadia@brakkamedia.com.au</li>
          <li>www.brakkamedia.com.au</li>
        </ul>
      </section>
    </article>
  </main>
</body>
</html>
```